Real Estate Wordpress Landing Page

I'm looking to a landing page dedicated to my real estate brokerage that's catered to promoting that my company provides 1.5% listings to home sellers... I have a couple examples that I'm really looking towards mocking in a version with similar color schemes using my current company colors/website.

http://lorvanta.com/
https://www.bluthorn.com/about/one-percent-listing-fee

My brokerage company website is http://www.calmridge.us/

Target Market(s)

real estate home sellers & buyers

Industry/Entity Type

Real Estate

Coding

Coded - Design and coding required

Number of Pages Required

1 page

Colors
3176b5
0255a3
eaf1f7
cedeed

Requirements
Must have
• Company website colors - http://www.calmridge.us/
• Something around the lines of this website page - http://lorvanta.com/
• Wordpress compatibility

```html
<!DOCTYPE html>
<html lang="en">
<head>
<meta charset="utf-8">
<title>Calmridge Realty</title>
<link href="https://fonts.googleapis.com/css2?family=Lato:wght@400;700;900&display=swap" rel="stylesheet">
<style>
:root{
  --blue:#0255a3;
  --blue-mid:#3176b5;
  --pale:#eaf1f7;
  --pale-2:#cedeed;
  --ink:#1e1e1e;
  --grey:#555;
  --line:#d7dde4;
  --dark:#2b2b2b;
}
*{box-sizing:border-box;margin:0;padding:0}
html,body{width:1200px;height:3267px;overflow:hidden}
body{font-family:'Lato',sans-serif;color:var(--ink);background:#fff;position:relative}
.wrap{width:1050px;margin:0 auto;position:relative}
a{color:inherit;text-decoration:none}

/* header */
.header{height:170px;position:relative;background:#fff}
.follow{position:absolute;right:76px;top:18px;display:flex;align-items:center;gap:14px;font-size:13px;font-weight:900;color:var(--blue);letter-spacing:.5px}
.dot{width:18px;height:18px;border-radius:50%;background:#4b5563;display:inline-block}
.brand{position:absolute;left:78px;top:70px;display:flex;align-items:center;gap:10px;font-size:26px;font-weight:700;color:var(--blue)}
.brand .sq{width:30px;height:30px;background:var(--blue)}
.info{position:absolute;top:92px;display:flex;align-items:center;gap:14px;font-size:14px;line-height:20px;color:#333}
.info .ic{width:40px;height:40px;border:1.5px solid #555;border-radius:50%;display:flex;align-items:center;justify-content:center}
.info .blue{color:var(--blue)}
.nav{height:54px;background:var(--blue);display:flex;align-items:center;justify-content:center;gap:34px;font-size:11.5px;font-weight:700;color:#fff;letter-spacing:.2px}

/* hero */
.hero{height:516px;position:relative;background:linear-gradient(180deg,#6f6656 0%,#8a7a61 40%,#5d5a4e 70%,#3a3a34 100%)}
.hero::after{content:"";position:absolute;inset:0;background:rgba(0,0,0,.25)}
.hero h1{position:absolute;top:196px;width:100%;text-align:center;font-size:48px;font-weight:900;color:#fff;letter-spacing:1px;z-index:2}
.arrow{position:absolute;top:208px;z-index:2}
.search{position:absolute;left:0;right:0;bottom:0;height:98px;background:rgba(0,0,0,.7);z-index:3}
.search .wrap{display:flex;gap:9px;padding-top:14px}
.field label{display:block;color:#fff;font-size:15px;font-weight:700;margin-bottom:8px}
.field .box{height:36px;background:#fff;font-size:12px;color:#444;display:flex;align-items:center;justify-content:space-between;padding:0 8px}
.btn-search{align-self:flex-end;width:136px;height:36px;background:var(--blue-mid);color:#fff;font-weight:900;font-size:17px;display:flex;align-items:center;justify-content:center;letter-spacing:.5px}

/* intro */
.intro{height:545px;text-align:center;padding-top:48px;position:relative}
.eyebrow{color:var(--blue);font-size:24px;font-weight:900}
.intro h2{font-size:20px;font-weight:900;margin-top:6px}
.intro p{font-size:16px;color:#444;line-height:24px;width:950px;margin:22px auto 0}
.intro .call{color:var(--blue);font-weight:900;font-size:16px;margin-top:18px}
.cities{display:flex;gap:32px;margin-top:20px}
.city{width:239px;border:1px solid var(--line);text-align:left}
.city .ph{height:184px}
.city span{display:block;text-align:center;font-size:14px;font-weight:900;padding:21px 0}
.side{position:absolute}

/* properties */
.props{height:614px;background:linear-gradient(90deg,var(--pale-2),var(--pale) 50%,var(--pale-2));padding-top:50px}
.tabs{display:flex;gap:6px}
.tab{height:60px;padding:0 28px;display:flex;align-items:center;font-size:16px;font-weight:900}
.tab.on{background:#fff;color:var(--blue)}
.tab.off{background:var(--blue);color:#fff}
.panel{background:#fff;height:442px;padding:42px 18px 0;display:flex;gap:39px}
.prop{width:313px}
.prop .ph{height:198px}
.prop h3{font-size:16px;font-weight:900;line-height:22px;margin-top:14px}
.prop .meta{font-size:14px;color:#555;margin-top:6px}
.prop .row{display:flex;justify-content:space-between;align-items:center;margin-top:18px}
.price{font-size:24px;font-weight:900;color:var(--blue)}
.icons{display:flex;gap:8px}
.icons i{width:22px;height:22px;border:1px solid #aaa;border-radius:3px;display:block}
.btn-out{height:42px;border:1.5px solid #bbb;margin-top:20px;display:flex;align-items:center;justify-content:center;font-size:14px;font-weight:700}

/* cta */
.cta{height:138px;background:var(--blue);color:#fff;text-align:center;padding-top:34px}
.cta h2{font-size:29px;font-weight:900;letter-spacing:.5px}
.cta p{font-size:22px;font-weight:700;margin-top:6px}

/* blog */
.blog{height:573px;padding-top:40px;position:relative}
.sec-title{text-align:center;color:var(--blue);font-size:22px;font-weight:900}
.posts{display:flex;gap:28px;margin-top:30px}
.post{width:331px}
.post .ph{height:198px}
.post h3{color:var(--blue);font-size:17px;font-weight:700;line-height:24px;margin-top:16px}
.post .by{font-size:14px;color:#444;margin-top:6px;display:flex;align-items:center;gap:6px}
.post p{font-size:14px;color:#444;line-height:22px;margin-top:12px}
.post .more{display:block;color:var(--blue);font-weight:900;font-size:15px;margin-top:16px}

/* vendors */
.vendors{height:254px;background:var(--pale);padding-top:46px;position:relative}
.vlist{display:flex;gap:32px;margin-top:34px}
.vendor{width:239px;height:90px;background:#fff;display:flex;align-items:center;justify-content:center}
.vendor i{display:block;background:var(--pale-2)}

/* footer */
.footer{height:344px;padding-top:40px;background:#fff}
.fcols{display:flex}
.fcol h4{color:var(--blue);font-size:15px;font-weight:900;letter-spacing:.3px}
.fcol p,.fcol li{font-size:13px;line-height:22px;color:#333}
.fcol ul{list-style:none;margin-top:10px}
.fcol li{display:flex;gap:12px;align-items:center}
.fbrand{display:flex;align-items:center;gap:8px;font-size:22px;font-weight:700;color:var(--blue);height:110px}
.fbrand .sq{width:26px;height:26px;background:var(--blue)}
.link{color:var(--blue);font-weight:900;font-size:14px}
.email{height:36px;border:1px solid #bbb;margin-top:18px;font-size:12px;display:flex;align-items:center;padding:0 12px;color:#555}
.signup{float:right;margin-top:14px;width:88px;height:34px;background:var(--blue);color:#fff;font-weight:900;font-size:12px;display:flex;align-items:center;justify-content:center}
.bottom{height:59px;background:var(--dark);color:#bbb;font-size:12px}
.bottom .wrap{display:flex;justify-content:space-between;align-items:center;height:59px}
</style>
</head>
<body>

<header class="header">
  <div class="follow">FOLLOW US: <i class="dot"></i><i class="dot"></i><i class="dot"></i><i class="dot"></i><i class="dot"></i></div>
  <div class="brand"><span class="sq"></span>Calmridge Realty</div>
  <div class="info" style="left:428px">
    <span class="ic"><svg width="16" height="16" viewBox="0 0 24 24"><path d="M6.6 10.8a15 15 0 006.6 6.6l2.2-2.2a1 1 0 011-.2 11 11 0 003.6.6 1 1 0 011 1V20a1 1 0 01-1 1A17 17 0 013 4a1 1 0 011-1h3.5a1 1 0 011 1 11 11 0 00.6 3.6 1 1 0 01-.3 1z" fill="#333"/></svg></span>
    <div><span class="blue">561-555-0142</span><br>contact@calmridge.us</div>
  </div>
  <div class="info" style="left:666px">
    <span class="ic"><svg width="14" height="18" viewBox="0 0 24 30"><path d="M12 0a10 10 0 00-10 10c0 8 10 20 10 20s10-12 10-20A10 10 0 0012 0zm0 14a4 4 0 110-8 4 4 0 010 8z" fill="#333"/></svg></span>
    <div>2400 Harbor Point Blvd, Ste 310<br>Boynton Beach, FL 33426</div>
  </div>
  <div class="info" style="left:938px">
    <span class="ic"><svg width="18" height="18" viewBox="0 0 24 24"><circle cx="12" cy="12" r="10" fill="none" stroke="#333" stroke-width="2"/><path d="M12 6v6l4 2" stroke="#333" stroke-width="2" fill="none"/></svg></span>
    <div>9 am to 5 pm<br>Monday thru Friday</div>
  </div>
</header>

<nav class="nav">
  <a>HOME</a><a>FEATURED CITIES</a><a>PROPERTY SEARCH</a><a>EMAIL ALERTS</a><a>COMMUNITIES</a><a>BUYERS &amp; SELLERS</a><a>RENTALS</a><a>INVESTING</a><a>CONTACT</a><a>CALMRIDGE</a>
</nav>

<section class="hero" role="img" aria-label="Two-storey Florida townhomes framed by tall pine trees">
  <svg class="arrow" style="left:76px" width="20" height="34" viewBox="0 0 20 34"><path d="M17 3L3 17l14 14" stroke="#fff" stroke-width="4" fill="none"/></svg>
  <h1>CALMRIDGE REALTY</h1>
  <svg class="arrow" style="right:76px" width="20" height="34" viewBox="0 0 20 34"><path d="M3 3l14 14L3 31" stroke="#fff" stroke-width="4" fill="none"/></svg>
  <div class="search"><div class="wrap">
    <div class="field" style="width:266px"><label>Location</label><div class="box">Enter City/zip code</div></div>
    <div class="field" style="width:132px"><label>Property Type</label><div class="box">House/Condo <span>⬍</span></div></div>
    <div class="field" style="width:132px"><label>Min. Price</label><div class="box">Select Price <span>⬍</span></div></div>
    <div class="field" style="width:132px"><label>Max. Price</label><div class="box">Select Price <span>⬍</span></div></div>
    <div class="field" style="width:100px"><label>Beds</label><div class="box">Select <span>⬍</span></div></div>
    <div class="field" style="width:100px"><label>Baths</label><div class="box">Select <span>⬍</span></div></div>
    <div class="btn-search">SEARCH</div>
  </div></div>
</section>

<section class="intro">
  <div class="eyebrow">BOYNTON BEACH REALTOR</div>
  <h2>DISCOVER SOME OF THE BEST COMMUNITIES IN PALM BEACH COUNTY, FL</h2>
  <p>Over here at Calmridge Realty, we have some of the best Realtors in the community who are ready to assist you and provide you with a free consultation.</p>
  <div class="call">Give us a call today! 561-555-0142</div>
  <svg class="side" style="left:44px;top:418px" width="14" height="24" viewBox="0 0 14 24"><path d="M12 2L2 12l10 10" stroke="#888" stroke-width="2.5" fill="none"/></svg>
  <svg class="side" style="right:44px;top:418px" width="14" height="24" viewBox="0 0 14 24"><path d="M2 2l10 10L2 22" stroke="#888" stroke-width="2.5" fill="none"/></svg>
  <div class="wrap cities">
    <div class="city"><div class="ph" role="img" aria-label="Mediterranean-style home with palm trees" style="background:linear-gradient(180deg,#6c9fd8,#b89a7a 55%,#5f7a44)"></div><span>Boca Raton Homes for Sale</span></div>
    <div class="city"><div class="ph" role="img" aria-label="White home with palms and lawn" style="background:linear-gradient(180deg,#4f86cf,#d9d4c8 55%,#4e7a3a)"></div><span>Jupiter Homes for Sale</span></div>
    <div class="city"><div class="ph" role="img" aria-label="Single-storey home behind palm trees" style="background:linear-gradient(180deg,#7fa9dc,#c3b28e 55%,#4d7d37)"></div><span>Palm Springs Homes for Sale</span></div>
    <div class="city"><div class="ph" role="img" aria-label="Large two-storey home with green lawn" style="background:linear-gradient(180deg,#3f78c8,#d4c6ad 55%,#3e7d2f)"></div><span>Boynton Beach Homes for Sale</span></div>
  </div>
</section>

<section class="props"><div class="wrap">
  <div class="tabs"><div class="tab on">PROPERTIES WE'VE SOLD</div><div class="tab off">PROPERTIES WE'VE RENTED</div></div>
  <div class="panel">
    <div class="prop"><div class="ph" role="img" aria-label="Two-storey beige house with garage" style="background:linear-gradient(180deg,#8fb4dc,#d8c9a6 50%,#5b7f3c)"></div>
      <h3>2817 Coral Ridge Ln, Delray Beach, FL 33484</h3><div class="meta">4 Bed &nbsp;|&nbsp; 3 Bath</div>
      <div class="row"><span class="price">$320,000</span><span class="icons"><i></i><i></i><i></i></span></div><div class="btn-out">VIEW DETAILS</div></div>
    <div class="prop"><div class="ph" role="img" aria-label="Single-storey house with driveway" style="background:linear-gradient(180deg,#4c88d2,#aab3b8 55%,#8d8f86)"></div>
      <h3>2817 Coral Ridge Ln, Delray Beach, FL 33484</h3><div class="meta">4 Bed &nbsp;|&nbsp; 3 Bath</div>
      <div class="row"><span class="price">$320,000</span><span class="icons"><i></i><i></i><i></i></span></div><div class="btn-out">VIEW DETAILS</div></div>
    <div class="prop"><div class="ph" role="img" aria-label="House with red tile roof and lawn" style="background:linear-gradient(180deg,#2e6a3a,#b8553c 45%,#d6cfc0 65%,#4f8a36)"></div>
      <h3>2817 Coral Ridge Ln, Delray Beach, FL 33484</h3><div class="meta">4 Bed &nbsp;|&nbsp; 3 Bath</div>
      <div class="row"><span class="price">$320,000</span><span class="icons"><i></i><i></i><i></i></span></div><div class="btn-out">VIEW DETAILS</div></div>
  </div>
</div></section>

<section class="cta">
  <h2>LIST FOR 1.5% COMMISSION,</h2>
  <p>And Receive Top Marketing from Harborline Pros!</p>
</section>

<section class="blog">
  <div class="sec-title">REAL ESTATE BLOG</div>
  <svg class="side" style="left:44px;top:300px" width="14" height="24" viewBox="0 0 14 24"><path d="M12 2L2 12l10 10" stroke="#888" stroke-width="2.5" fill="none"/></svg>
  <svg class="side" style="right:44px;top:300px" width="14" height="24" viewBox="0 0 14 24"><path d="M2 2l10 10L2 22" stroke="#888" stroke-width="2.5" fill="none"/></svg>
  <div class="wrap posts">
    <article class="post"><div class="ph" role="img" aria-label="Aerial view of a beachfront skyline" style="background:linear-gradient(180deg,#9cc6ec,#d9e4ea 40%,#3fb3c4 70%,#e6dcc2)"></div>
      <h3>Skills That You Can Learn In The Real Estate Market</h3><div class="by">&#9679; By Marcel Duvane</div>
      <p>Lorem ipsum dolor sit amet, consectetur adipiscing elit. Duis mollis et sem sed sollicitudin...</p><a class="more">Read More</a></article>
    <article class="post"><div class="ph" role="img" aria-label="White Spanish-style villa with lawn" style="background:linear-gradient(180deg,#3e7fd0,#e9e4dc 50%,#4f8b3a)"></div>
      <h3>Skills That You Can Learn In The Real Estate Market</h3><div class="by">&#9679; By Marcel Duvane</div>
      <p>Lorem ipsum dolor sit amet, consectetur adipiscing elit. Duis mollis et sem sed sollicitudin...</p><a class="more">Read More</a></article>
    <article class="post"><div class="ph" role="img" aria-label="Modern home with pool at dusk" style="background:linear-gradient(180deg,#5b6e86,#d8b98c 50%,#36b2d6)"></div>
      <h3>Skills That You Can Learn In The Real Estate Market</h3><div class="by">&#9679; By Marcel Duvane</div>
      <p>Lorem ipsum dolor sit amet, consectetur adipiscing elit. Duis mollis et sem sed sollicitudin...</p><a class="more">Read More</a></article>
  </div>
</section>

<section class="vendors">
  <div class="sec-title">OUR VENDORS</div>
  <svg class="side" style="left:44px;top:144px" width="14" height="24" viewBox="0 0 14 24"><path d="M12 2L2 12l10 10" stroke="#888" stroke-width="2.5" fill="none"/></svg>
  <svg class="side" style="right:44px;top:144px" width="14" height="24" viewBox="0 0 14 24"><path d="M2 2l10 10L2 22" stroke="#888" stroke-width="2.5" fill="none"/></svg>
  <div class="wrap vlist">
    <div class="vendor"><i style="width:140px;height:24px"></i></div>
    <div class="vendor"><i style="width:130px;height:28px"></i></div>
    <div class="vendor"><i style="width:120px;height:50px"></i></div>
    <div class="vendor"><i style="width:124px;height:34px"></i></div>
  </div>
</section>

<footer class="footer"><div class="wrap fcols">
  <div class="fcol" style="width:393px">
    <div class="fbrand"><span class="sq"></span>Calmridge Realty</div>
    <p style="width:340px;margin-top:14px">Calmridge Realty is a Boynton Beach real estate company that prides in our superior service when it comes to helping our clients buy a home, sell a home or rent a home in the Palm Beach County and Broward County areas..</p>
    <p class="link" style="margin-top:10px">Read More &rsaquo;&rsaquo;</p>
  </div>
  <div class="fcol" style="width:326px">
    <h4>CONTACT INFO</h4>
    <p style="margin-top:10px">2400 Harbor Point Blvd, Ste 310,<br>Boynton Beach,<br>FL 33426</p>
    <ul>
      <li><span>&#9990;</span>561-555-0142</li>
      <li><span>&#9113;</span>561-555-0187</li>
      <li><span>&#9993;</span>contact@calmridge.us</li>
    </ul>
    <p class="link" style="margin-top:10px">Contact Us &rsaquo;&rsaquo;</p>
  </div>
  <div class="fcol" style="width:331px">
    <h4>NEWSLETTER SIGN UP</h4>
    <p style="margin-top:10px">The Calmridge Realty team is dedicated to keeping you up to date with the real estate market.</p>
    <div class="email">Enter Email Address</div>
    <div class="signup">SIGN UP</div>
    <h4 style="clear:both;padding-top:24px">FOLLOW US</h4>
    <div style="display:flex;gap:20px;margin-top:12px"><i class="dot"></i><i class="dot"></i><i class="dot"></i><i class="dot"></i><i class="dot"></i></div>
  </div>
</div></footer>

<div class="bottom"><div class="wrap">
  <span>Copyright &copy; 2018, Calmridge.us - All rights reserved.</span>
  <span>Privacy / Terms and Conditions / Contact Us / Mobile Notary</span>
</div></div>

</body>
</html>
```